Dential Clinic Business Card

We need a simple elegant business card. 2 sided. First side with our details, and 2nd side with appointment time rows.

Dark background preferred. Will consider monotone design, or colored. Surprise us.

Details:
SIDE1

Harwick Plaza Dental

Dr Milo Brent
BDSc(Tarn) MOPRVS

Shop 42, Harwick Plaza
8-22 Larch Avenue, Larchmont VIC 3190
Phone: 03 9447 2835
email: info@harwickplazadental.com.au
site: www.harwickplazadental.com.au
_____________________________________
SIDE 2
Appointed Time ________________________
Notes _______________________

Target Market(s)

Dental Patients

Industry/Entity Type

Healthcare

Contact Information for Business Card

SIDE1

Harwick Plaza Dental

Dr Milo Brent
Shop 42, Harwick Plaza
Phone: 03 9447 2835
SIDE 2

Font styles to use
Other font styles liked:
• Comfortaa

Requirements
Must have
• Dr Milo Brent
BDSc(Tarn) MOPRVS

Address
Phone
Email
Website
Nice to have
• Simple elegant design with our logo.
Colored logo.
Light text on dark background - Side 1
Light background so can be written on with dark pen - SIde 2
Should not have
• Too many colors

```html
<!DOCTYPE html>
<html lang="en">
<head>
<meta charset="utf-8">
<title>Harwick Plaza Dental – Business Card</title>
<link href="https://fonts.googleapis.com/css2?family=Comfortaa:wght@400;600;700&display=swap" rel="stylesheet">
<style>
  :root {
    --page-bg: #1b1c1e;
    --card-bg: #2b2c2e;
    --card-edge: #343538;
    --brand-blue: #2a93d8;
    --brand-green: #7dc143;
    --text-light: #d4d5d7;
    --text-muted: #a9abae;
    --pill-bg: #ffffff;
    --pill-text: #3a3b3d;
    --dots: #7b7d80;
  }
  * { box-sizing: border-box; margin: 0; padding: 0; }
  html, body {
    width: 1200px; height: 800px; overflow: hidden;
    background: var(--page-bg);
    font-family: "Comfortaa", sans-serif;
  }
  .sheet {
    width: 1200px; height: 800px;
    display: flex; flex-direction: column;
    align-items: center; justify-content: center; gap: 32px;
  }
  .card {
    position: relative;
    width: 620px; height: 354px;
    background: var(--card-bg);
    border: 1px solid var(--card-edge);
    border-radius: 18px;
    overflow: hidden;
  }
  .brand {
    position: absolute;
    display: flex; align-items: center; gap: 12px;
  }
  .brand-dot {
    width: 16px; height: 16px; border-radius: 50%;
    background: var(--brand-green);
  }
  .brand-name {
    font-weight: 700; font-size: 30px; letter-spacing: 1px;
    color: var(--brand-green); text-transform: uppercase;
    white-space: nowrap;
  }

  /* appointment side */
  .card--appointments .brand { left: 40px; top: 42px; }
  .appointment-list {
    position: absolute; left: 40px; right: 40px; top: 118px;
    display: flex; flex-direction: column; gap: 22px;
  }
  .appointment-row {
    background: var(--pill-bg);
    border-radius: 44px;
    padding: 16px 34px 14px;
    color: var(--pill-text);
    font-size: 15px;
    display: grid; grid-template-columns: 1fr 1fr; column-gap: 18px; row-gap: 8px;
  }
  .field { display: flex; align-items: baseline; gap: 6px; }
  .field--wide { grid-column: 1 / -1; }
  .field-line { flex: 1; border-bottom: 2px dotted var(--dots); height: 1px; }

  /* details side */
  .card--details .brand { left: 40px; top: 36px; }
  .details {
    position: absolute; left: 40px; right: 40px; bottom: 28px;
    color: var(--text-light);
  }
  .dentist-name {
    color: var(--brand-blue); font-weight: 600;
    font-size: 22px; line-height: 1.2; text-transform: uppercase; margin-bottom: 4px;
  }
  .credentials {
    color: var(--text-muted); font-size: 13px; letter-spacing: 0.5px;
    margin-bottom: 12px;
  }
  .address { font-size: 15px; line-height: 1.5; margin-bottom: 12px; }
  .contact-list { list-style: none; font-size: 15px; line-height: 1.6; }
  .contact-list li { display: flex; align-items: center; gap: 10px; }
  .contact-icon { width: 14px; height: 14px; flex: none; }
</style>
</head>
<body>
<main class="sheet">

  <section class="card card--appointments" aria-label="Appointment side">
    <div class="brand">
      <span class="brand-dot"></span>
      <span class="brand-name">Harwick Plaza Dental</span>
    </div>
    <div class="appointment-list">
      <div class="appointment-row">
        <div class="field"><span>Time</span><span class="field-line"></span></div>
        <div class="field"><span>Date</span><span class="field-line"></span></div>
        <div class="field field--wide"><span>Notes</span><span class="field-line"></span></div>
      </div>
      <div class="appointment-row">
        <div class="field"><span>Time</span><span class="field-line"></span></div>
        <div class="field"><span>Date</span><span class="field-line"></span></div>
        <div class="field field--wide"><span>Notes</span><span class="field-line"></span></div>
      </div>
    </div>
  </section>

  <section class="card card--details" aria-label="Details side">
    <div class="brand">
      <span class="brand-dot"></span>
      <span class="brand-name">Harwick Plaza Dental</span>
    </div>
    <div class="details">
      <h1 class="dentist-name">Dr Milo Brent</h1>
      <p class="credentials">BDSc(Tarn) MOPRVS</p>
      <p class="address">Shop 42, Harwick Plaza<br>8-22 Larch Avenue, Larchmont VIC 3190</p>
      <ul class="contact-list">
        <li>
          <svg class="contact-icon" viewBox="0 0 24 24" aria-hidden="true"><path fill="#2a93d8" d="M6.6 10.8a15.1 15.1 0 0 0 6.6 6.6l2.2-2.2c.3-.3.7-.4 1-.2 1.1.4 2.3.6 3.6.6.6 0 1 .4 1 1V20c0 .6-.4 1-1 1A17 17 0 0 1 3 4c0-.6.4-1 1-1h3.5c.6 0 1 .4 1 1 0 1.3.2 2.5.6 3.6.1.3 0 .7-.2 1z"/></svg>
          <span>03 9447 2835</span>
        </li>
        <li>
          <svg class="contact-icon" viewBox="0 0 24 24" aria-hidden="true"><rect x="2" y="5" width="20" height="14" rx="2" fill="#2a93d8"/><path d="M3 6l9 7 9-7" fill="none" stroke="#2b2c2e" stroke-width="2"/></svg>
          <span>info@harwickplazadental.com.au</span>
        </li>
        <li>
          <svg class="contact-icon" viewBox="0 0 24 24" aria-hidden="true"><circle cx="12" cy="12" r="10" fill="#2a93d8"/><path d="M2 12h20M12 2c3 3 3 17 0 20M12 2c-3 3-3 17 0 20" fill="none" stroke="#2b2c2e" stroke-width="1.5"/></svg>
          <span>www.harwickplazadental.com.au</span>
        </li>
      </ul>
    </div>
  </section>

</main>
</body>
</html>
```